Web Design for Recruitment Agency

We need a new web design for the company who provides professional services in Labor Recruitment and Home Helpers Hire.

The sections to be covered:
1. About us
2. Philosophy
3. Services
- Labor Recruitment
* skilled workers
* unskilled workers
- Home Helpers
4. Search CV
5. Testimonials
5. Contact us

Examples:
http://www.qorvennaue.com
http://tpmubelo.ae

The website should be clean and elegant. It should portray professionalism and attention to details.

It is important to have interactive and easy-to-navigate design with lots of pictures.

We want clients to get the right impression and be able to request a contact in case they have a requirement. We also want clients to be able to search for CVs that are already in the database. CV should be displayed as a profile card (photo and brief information about the candidate).

Logo is attached.

Target Market(s)

Local families, companies.

Industry/Entity Type

It Company

Number of Pages Required

1 page

Font styles to use
Sans Serif

Requirements
Must have
• Clean layout with pictures
Nice to have
• Dynamic, engaging website.

```html
<!DOCTYPE html>
<html lang="en">
<head>
<meta charset="utf-8">
<title>KVT – Professional Services</title>
<link rel="stylesheet" href="https://fonts.googleapis.com/css2?family=Alegreya+Sans:wght@300;400;500&display=swap">
<style>
:root{
  --bg:#ffffff;
  --panel:#ececec;
  --text:#777777;
  --text-dark:#444444;
  --rule:#c9c9c9;
  --white:#ffffff;
  --hero-a:#3a3a3a;
  --hero-b:#d9d6d9;
  --hero-c:#b9b4ba;
  --photo-a:#8b8f95;
  --photo-b:#d7dde2;
  --photo-c:#c9b79a;
  --photo-d:#e8e6df;
}
*{box-sizing:border-box;margin:0;padding:0}
html,body{width:1200px;height:750px;overflow:hidden;background:var(--bg);
  font-family:"Alegreya Sans",sans-serif;color:var(--text)}
.page{position:relative;width:1200px;height:750px}
.abs{position:absolute}

.site-header{left:0;top:0;width:1200px;height:70px;background:var(--panel);border-bottom:3px solid #d4d4d4}
.brand{left:10px;top:5px;display:flex;align-items:center;gap:6px;height:60px}
.brand-mark{width:14px;height:14px;border-radius:50%;background:#2f7d4a}
.brand-name{font-size:22px;font-weight:500;color:var(--text-dark)}
.contact-phone{left:128px;top:12px;display:flex;align-items:center;gap:6px;font-size:15px;font-weight:300}
.contact-address{left:288px;top:13px;display:flex;align-items:center;gap:12px;font-size:16px;font-weight:300;line-height:20px}
.main-nav{right:3px;top:10px;height:55px;display:flex;align-items:stretch}
.main-nav a{display:flex;align-items:center;padding:0 7px;font-size:17px;color:var(--text);text-decoration:none;border-left:1px solid #d3d3d3}
.main-nav a:first-child{border-left:none}

.hero{left:0;top:72px;width:1200px;height:224px;
  background:linear-gradient(90deg,var(--hero-a) 0%,#b98a78 18%,var(--hero-b) 45%,#e6e3e8 70%,var(--hero-c) 100%)}
.hero-title{left:0;top:142px;width:1186px;text-align:center;font-size:50px;font-weight:300;color:var(--white)}
.hero-cta{left:454px;top:216px;width:257px;height:52px;border:3px solid var(--white);
  display:flex;align-items:center;justify-content:center;font-size:32px;font-weight:300;color:var(--white)}

.photo-staff{left:7px;top:303px;width:435px;height:194px;background:linear-gradient(120deg,var(--photo-a),var(--photo-b) 60%,#4a4a4a)}
.photo-care{left:454px;top:497px;width:327px;height:178px;background:linear-gradient(135deg,var(--photo-c),var(--photo-d) 55%,#aab79a)}

.how-title{left:457px;top:298px;font-size:32px;font-weight:400}
.how-text{left:457px;top:341px;width:560px;font-size:15.8px;line-height:20.5px;font-weight:400}

.join-title{left:7px;top:503px;width:435px;text-align:center;font-size:19px;color:var(--text-dark)}
.join-sub{left:7px;top:527px;width:435px;text-align:center;font-size:12px;color:#555}
.field{left:8px;width:434px;height:35px;background:var(--panel);padding-left:14px;display:flex;align-items:center;font-size:16px;font-weight:300;color:#999}
.btn{background:var(--panel);display:flex;align-items:center;justify-content:center;color:var(--text)}
.register{left:8px;top:641px;width:434px;height:34px;font-size:16px}

.ask-title{left:792px;top:490px;font-size:34px}
.message{left:792px;top:532px;width:326px;height:143px;background:var(--panel);border-top:2px solid var(--rule);padding:5px 6px;font-size:12px;font-weight:300;color:#999}
.send{left:1123px;top:651px;width:71px;height:24px;font-size:12px}

.site-footer{left:0;top:700px;width:1200px;height:50px;background:var(--panel);display:flex;align-items:center;justify-content:center;font-size:16px;color:var(--text-dark)}
</style>
</head>
<body>
<div class="page">
  <header class="site-header abs">
    <div class="brand abs"><span class="brand-mark"></span><span class="brand-name">KVT</span></div>
    <div class="contact-phone abs">
      <svg width="46" height="46" viewBox="0 0 24 24" aria-hidden="true"><path fill="#666" d="M6.6 10.8c1.4 2.8 3.8 5.1 6.6 6.6l2.2-2.2c.3-.3.7-.4 1-.2 1.1.4 2.3.6 3.6.6.6 0 1 .4 1 1V20c0 .6-.4 1-1 1C10.6 21 3 13.4 3 4c0-.6.4-1 1-1h3.5c.6 0 1 .4 1 1 0 1.3.2 2.5.6 3.6.1.3 0 .7-.2 1z"/></svg>
      <span>+848 555 010</span>
    </div>
    <div class="contact-address abs">
      <svg width="46" height="40" viewBox="0 0 24 21" aria-hidden="true"><path fill="#666" d="M12 1 1 11h3v9h6v-6h4v6h6v-9h3z"/></svg>
      <span>Harbor City<br>207/31</span>
    </div>
    <nav class="main-nav abs">
      <a href="#about">About us</a><a href="#philosophy">Philosophy</a><a href="#services">Services</a><a href="#cv">Search CV</a><a href="#testimonials">Testimonials</a><a href="#contact">Contact us</a>
    </nav>
  </header>

  <section class="hero abs" role="img" aria-label="Photo of a cleaner wiping a window"></section>
  <h1 class="hero-title abs">Proffesional services</h1>
  <a class="hero-cta abs">request contact</a>

  <div class="photo-staff abs" role="img" aria-label="Photo of smiling cleaning staff at work in an office"></div>
  <h2 class="how-title abs">How it works?</h2>
  <p class="how-text abs">In collaboration with the customer we work closely to understand precisely what is needed and provide a professional, transparent and tailored cleaning solution. Encom­passing a range of service solutions enables the customer to scale their services to meet their ever changing needs. Across the globe our services offer excellence founded on specialist knowledge and expertise, documented processes and the ability to estab­lish and share best practices across national boundaries and continents.</p>

  <h3 class="join-title abs">Qualified staff</h3>
  <p class="join-sub abs">Send us your CV and become a member</p>
  <div class="field abs" style="top:551px">Your email adress...</div>
  <div class="field abs" style="top:597px">Phone number...</div>
  <div class="btn register abs">Register</div>

  <div class="photo-care abs" role="img" aria-label="Photo of a caregiver with an elderly woman in a wheelchair"></div>
  <h2 class="ask-title abs">If you have any questions</h2>
  <div class="message abs">Write here...</div>
  <div class="btn send abs">Send</div>

  <footer class="site-footer abs">Copyright 2015 KVT</footer>
</div>
</body>
</html>
```